Ondas Tierra - Stationery and Presentation Materials
Biz card, letterhead, envelope, presentation folder
Bright & Fun-filled
Martin Coble
E.S.
Tel. +503.2417.8836
Cel. +503.7396.1052
U.S. +1.800.555.0147 x3061
U.S.
ondastierra.led@correoplano.com
PLEASE, DON'T POST EMAIL IN DRAFTS.
--The business is rental of large LED screens for visuals, which are made of thousands of tiny lights.
---Please give a range of crazy/abstract as well as aggressive but traditional/corporate concepts for all items in subtitle.
---The presentation folder is to digitally insert fotos later for printing. Borders are key. A CD will be included, on a plastic peg anywhere in the folder, and CD design must blend with folder graphics on the point where CD sits.
Minimal.
---try wrap-around logo
----1 "wild concept" if anyone is willing - background is very tiny, SHINING, white lights (almost pixel-looking), with the logo symbol on top.

```html
<!DOCTYPE html>
<html lang="en">
<head>
<meta charset="utf-8">
<title>Ondas Tierra — Stationery and Presentation Materials</title>
<link href="https://fonts.googleapis.com/css2?family=Open+Sans:ital,wght@0,400;0,700;0,800;1,700&display=swap" rel="stylesheet">
<style>
  :root {
    --paper: #ffffff;
    --blue-deep: #123f96;
    --blue: #1f5fbf;
    --blue-light: #3b8fe0;
    --orange: #f47a20;
    --red: #e3342b;
    --yellow: #f7b51c;
    --ink: #3a3a3a;
    --grey: #9aa0a8;
  }
  html, body { margin: 0; padding: 0; overflow: hidden; background: var(--paper); }
  .canvas { width: 1200px; height: 466px; display: block; }
  text { font-family: "Open Sans", Arial, sans-serif; }
  .brand { font-weight: 800; fill: var(--red); }
  .brand-light { font-weight: 800; fill: var(--paper); }
  .person { font-weight: 700; font-style: italic; fill: var(--orange); }
  .person-light { font-weight: 700; font-style: italic; fill: var(--paper); }
  .contact { font-size: 5.5px; fill: var(--paper); }
  .contact-dark { font-size: 5.5px; fill: var(--ink); }
  .salutation { font-size: 7px; fill: var(--grey); }
</style>
</head>
<body>
<svg class="canvas" viewBox="0 0 1200 466" xmlns="http://www.w3.org/2000/svg">
  <defs>
    <linearGradient id="blue-field" x1="0" y1="0" x2="1" y2="1">
      <stop offset="0" stop-color="var(--blue-deep)"/>
      <stop offset="1" stop-color="var(--blue-light)"/>
    </linearGradient>
    <linearGradient id="folder-field" x1="0" y1="0" x2="0" y2="1">
      <stop offset="0" stop-color="var(--blue-deep)"/>
      <stop offset="0.55" stop-color="var(--blue)"/>
      <stop offset="0.8" stop-color="var(--red)"/>
      <stop offset="1" stop-color="var(--orange)"/>
    </linearGradient>
    <linearGradient id="warm-wave" x1="0" y1="0" x2="1" y2="0">
      <stop offset="0" stop-color="var(--red)"/>
      <stop offset="0.6" stop-color="var(--orange)"/>
      <stop offset="1" stop-color="var(--yellow)"/>
    </linearGradient>
    <linearGradient id="pocket-field" x1="0" y1="0" x2="0" y2="1">
      <stop offset="0" stop-color="var(--orange)"/>
      <stop offset="1" stop-color="var(--yellow)"/>
    </linearGradient>
    <radialGradient id="lights-glow" cx="0.5" cy="0.5" r="0.5">
      <stop offset="0" stop-color="#ffffff" stop-opacity="0.35"/>
      <stop offset="1" stop-color="#ffffff" stop-opacity="0"/>
    </radialGradient>
  </defs>

  <!-- Business card, front -->
  <g class="card-front">
    <rect x="14" y="53" width="154" height="96" rx="6" fill="var(--paper)" stroke="#e2e2e2"/>
    <rect x="24" y="64" width="10" height="10" fill="var(--orange)"/>
    <text class="brand" x="38" y="73" font-size="11">Ondas Tierra</text>
    <text class="person" x="100" y="96" font-size="9">Martin Coble</text>
    <path d="M14 112 C60 100 110 124 168 106 V143 a6 6 0 0 1 -6 6 H20 a6 6 0 0 1 -6 -6 Z" fill="url(#warm-wave)"/>
    <path d="M14 118 C60 108 110 130 168 114" fill="none" stroke="var(--paper)" stroke-width="1.5"/>
    <text class="contact" x="22" y="129">Tel. +503.2417.8836  ·  Cel. +503.7396.1052</text>
    <text class="contact" x="22" y="137">U.S. +1.800.555.0147 x3061</text>
    <text class="contact" x="22" y="145">ondastierra.led@correoplano.com</text>
  </g>

  <!-- Business card, back -->
  <g class="card-back">
    <rect x="14" y="163" width="150" height="90" rx="6" fill="url(#blue-field)"/>
    <ellipse cx="110" cy="225" rx="50" ry="28" fill="url(#lights-glow)" role="img" aria-label="Field of tiny shining LED lights"/>
    <rect x="26" y="186" width="11" height="11" fill="var(--orange)"/>
    <text class="brand-light" x="42" y="196" font-size="12">Ondas Tierra</text>
  </g>

  <!-- CD -->
  <g class="cd">
    <circle cx="205" cy="197" r="43" fill="var(--paper)" stroke="#d6d6d6"/>
    <path d="M165 185 C185 170 215 205 246 186 A43 43 0 0 1 205 240 A43 43 0 0 1 165 185 Z" fill="url(#blue-field)"/>
    <path d="M166 205 C188 192 215 222 247 202" fill="none" stroke="var(--orange)" stroke-width="5"/>
    <circle cx="205" cy="197" r="10" fill="var(--paper)" stroke="#cfcfcf"/>
    <circle cx="205" cy="197" r="4" fill="#e9e9e9"/>
    <text class="brand" x="180" y="175" font-size="7">Ondas Tierra</text>
  </g>

  <!-- Envelope -->
  <g class="envelope" transform="rotate(-2 220 340)">
    <rect x="144" y="281" width="152" height="116" fill="var(--paper)" stroke="#e0e0e0"/>
    <rect x="154" y="291" width="9" height="9" fill="var(--orange)"/>
    <text class="brand" x="167" y="299" font-size="9">Ondas Tierra</text>
    <path d="M144 330 C190 316 240 342 296 324 V397 H144 Z" fill="url(#blue-field)"/>
    <path d="M144 338 C190 326 240 350 296 334" fill="none" stroke="var(--orange)" stroke-width="4"/>
    <path d="M144 370 C190 360 240 380 296 366 V397 H144 Z" fill="url(#warm-wave)"/>
    <text class="contact" x="152" y="356">Tel. +503.2417.8836</text>
    <text class="contact" x="152" y="363">ondastierra.led@correoplano.com</text>
  </g>

  <!-- Letterhead -->
  <g class="letterhead">
    <rect x="355" y="53" width="185" height="360" fill="var(--paper)" stroke="#e0e0e0"/>
    <rect x="366" y="66" width="12" height="12" fill="var(--orange)"/>
    <text class="brand" x="383" y="77" font-size="13">Ondas Tierra</text>
    <text class="salutation" x="366" y="100">Lorem ipsum dolor sit amet</text>
    <rect x="450" y="290" width="60" height="60" fill="var(--orange)" opacity="0.12"/>
    <path d="M355 360 C400 346 470 372 540 352 V413 H355 Z" fill="url(#blue-field)"/>
    <path d="M355 370 C400 358 470 382 540 364" fill="none" stroke="var(--orange)" stroke-width="5"/>
    <text class="contact" x="366" y="392">Tel. +503.2417.8836  ·  Cel. +503.7396.1052</text>
    <text class="contact" x="366" y="400">U.S. +1.800.555.0147 x3061</text>
    <text class="contact" x="366" y="408">ondastierra.led@correoplano.com</text>
  </g>

  <!-- Presentation folder -->
  <g class="folder">
    <!-- back cover -->
    <rect x="624" y="14" width="264" height="430" fill="url(#folder-field)"/>
    <ellipse cx="760" cy="200" rx="120" ry="120" fill="url(#lights-glow)" role="img" aria-label="Field of tiny shining LED lights"/>
    <rect x="710" y="140" width="100" height="100" fill="var(--paper)" opacity="0.12"/>
    <text class="contact" x="636" y="410">Tel. +503.2417.8836  ·  Cel. +503.7396.1052</text>
    <text class="contact" x="636" y="418">U.S. +1.800.555.0147 x3061</text>
    <text class="contact" x="636" y="426">ondastierra.led@correoplano.com</text>

    <!-- front cover -->
    <rect x="895" y="14" width="210" height="430" fill="url(#folder-field)"/>
    <path d="M895 14 H1105 V78 C1040 92 960 70 895 86 Z" fill="var(--paper)"/>
    <rect x="906" y="34" width="13" height="13" fill="var(--orange)"/>
    <text class="brand" x="924" y="46" font-size="15">Ondas Tierra</text>
    <text class="person-light" x="906" y="114" font-size="14">Martin Coble</text>
    <ellipse cx="1000" cy="200" rx="90" ry="90" fill="url(#lights-glow)" role="img" aria-label="Field of tiny shining LED lights"/>
    <rect x="960" y="150" width="90" height="90" fill="var(--paper)" opacity="0.12"/>

    <!-- inside pocket -->
    <path d="M1105 216 H1193 V444 H1105 Z" fill="url(#pocket-field)"/>
    <path d="M1105 216 C1140 210 1170 230 1193 222" fill="none" stroke="var(--paper)" stroke-width="2"/>
    <path d="M895 330 C960 316 1040 344 1193 318 V444 H895 Z" fill="url(#pocket-field)" opacity="0.9"/>
    <text class="contact" x="906" y="410">Tel. +503.2417.8836  ·  Cel. +503.7396.1052</text>
    <text class="contact" x="906" y="418">U.S. +1.800.555.0147 x3061</text>
    <text class="contact" x="906" y="426">ondastierra.led@correoplano.com</text>
  </g>
</svg>
</body>
</html>
```